Create a memorable Web Design for real estate branding

we are a Minnepolis brokerage and boutique housing specialist with over 27 years of experience in the Global furnished housing industry, servicing the Greater Los Angeles area. Specializing in “warm environments” we offer a customized approach to satisfying our guests and client’s needs by offering a wide array of options in highly desirable areas. Additionally, Lantern Dwelling Partners offers assistance and expertise to home buyers, sellers and investors.

Industry/Entity Type

Real Estate

Number of Pages Required

1 page

Font styles to use
Serif
Sans Serif
Decorative

```html
<!DOCTYPE html>
<html lang="en">
<head>
<meta charset="utf-8">
<title>Lantern Dwelling Partners</title>
<link rel="stylesheet" href="https://fonts.googleapis.com/css2?family=Cinzel:wght@400;600&family=Raleway:wght@400;500;600;700&family=Open+Sans:wght@400;600&display=swap">
<style>
:root{
  --teal:#0ea88f;
  --teal-dark:#0b8f7a;
  --lime:#8dc63f;
  --lime-light:#a6d45a;
  --ink:#2b2b2b;
  --muted:#555;
  --header:rgba(18,26,28,.88);
  --dark:#2a3133;
  --panel:#f1f1f1;
  --line:#d8d8d8;
  --white:#fff;
}
*{box-sizing:border-box;margin:0;padding:0}
html,body{width:1200px;height:2687px;overflow:hidden}
body{position:relative;font-family:"Open Sans",Arial,sans-serif;color:var(--ink);background:var(--white)}
h2,h3{font-weight:400}
.abs{position:absolute}
.ph{position:absolute;display:block}

/* hero */
.hero{left:0;top:0;width:1200px;height:616px;background:linear-gradient(110deg,#6d4b3a 0%,#b98c6c 25%,#d9c4ad 45%,#c2463f 62%,#8d7f78 80%,#4f5b63 100%)}
.header{left:0;top:0;width:1200px;height:129px;background:var(--header)}
.logo{left:102px;top:38px;font-family:"Raleway",sans-serif;font-weight:700;color:var(--lime);font-size:34px;line-height:38px}
.consult{left:815px;top:0;width:268px;height:34px;background:var(--teal);border:2px solid #d9f2ee;border-top:0;color:#fff;font-family:"Cinzel",serif;font-size:17px;text-align:center;line-height:32px}
.contact-top{left:708px;top:50px;color:#fff;font-size:14px;display:flex;align-items:center;gap:8px}
.nav{left:433px;top:90px;display:flex;font-family:"Cinzel",serif;font-size:16px;color:#fff}
.nav a{color:#fff;text-decoration:none;padding:0 13px;border-left:1px solid rgba(255,255,255,.5);line-height:18px}
.nav a:first-child{border-left:0;color:var(--lime-light);padding-left:0}
.slider-arrow{left:0;top:342px;width:36px;height:34px;background:rgba(0,0,0,.7);border-radius:0 4px 4px 0}

.tabs{left:100px;top:424px;display:flex}
.tabs span{height:34px;line-height:34px;padding:0 18px;background:var(--lime);color:#1d2a10;font-size:16px;margin-right:3px}
.tabs span.on{background:var(--teal);color:#0b2a22}
.search{left:100px;top:458px;width:665px;height:151px;background:rgba(25,25,25,.72);border-radius:0 8px 8px 8px}
.search .field{left:18px;top:22px;width:522px;height:38px;background:#fff;font-size:14px;line-height:38px;padding-left:12px;color:#333}
.search .btn{left:550px;top:22px;width:90px;height:38px;background:#555;color:#fff;font-size:14px;line-height:38px;text-align:center}
.search label{position:absolute;top:74px;color:#eee;font-size:12px}
.sel{position:absolute;top:100px;height:30px;background:#fff;font-size:12px;line-height:30px;padding-left:8px;color:#333}
.sel::after{content:"";position:absolute;right:10px;top:12px;border:6px solid transparent;border-top-color:var(--lime)}

/* about */
.about-img{left:102px;top:661px;width:236px;height:269px;background:linear-gradient(135deg,#e7ecef,#9aa7b1 55%,#3a3f47)}
.h2{font-family:"Raleway",sans-serif;font-size:23px;color:var(--ink);font-weight:500}
.about{left:353px;top:655px;width:395px}
.about .rule{height:2px;background:var(--line);margin:6px 0 12px;position:relative}
.about .rule::before{content:"";position:absolute;left:0;top:0;width:60px;height:2px;background:var(--teal)}
.about p{font-size:13.4px;line-height:20px;color:#444}
.ticks{list-style:none;margin-top:10px}
.ticks li{font-size:12px;line-height:17px;color:#333;padding-left:22px;position:relative;margin-bottom:7px}
.ticks svg{position:absolute;left:0;top:2px}
.btn-teal{display:inline-block;background:var(--teal);color:#fff;font-size:12px;padding:10px 16px;margin-top:4px}
.offers{left:796px;top:655px;width:302px}
.offers .rule{height:2px;background:var(--line);margin:6px 0 18px}
.offer{display:flex;gap:14px;margin-bottom:22px}
.offer .ic{width:40px;height:38px;border:1px solid var(--line);flex:none;display:flex;align-items:center;justify-content:center}
.offer b{font-size:12px;display:block;margin-bottom:2px;font-weight:600}
.offer span{font-size:11px;line-height:15px;color:#444}

/* featured */
.featured-bg{left:0;top:980px;width:1200px;height:274px;background:linear-gradient(180deg,#3a4144,#20272a)}
.feat-title{left:0;top:1013px;width:1200px;text-align:center;color:#fff;font-family:"Raleway",sans-serif;font-weight:400;font-size:22px}
.feat-rule{left:402px;top:1062px;width:396px;height:1px;background:rgba(255,255,255,.5)}
.feat-rule::before{content:"";position:absolute;left:168px;top:-1px;width:60px;height:3px;background:var(--teal)}
.card{position:absolute;top:1112px;width:228px;height:303px;background:#fff;border:1px solid #ddd}
.card .ph{left:8px;top:8px;width:210px;height:127px}
.card .t{position:absolute;left:8px;top:148px;font-size:13.5px}
.card .s{position:absolute;left:8px;top:172px;font-size:12px;color:#777}
.card .tag{position:absolute;left:8px;top:222px;height:25px;line-height:25px;padding:0 10px;font-size:12px;color:#fff;border-radius:2px}
.tag.rent{background:var(--teal)}
.tag.dark{background:#333}
.card .price{position:absolute;right:10px;top:218px;color:var(--teal);font-size:22px;font-family:"Raleway",sans-serif}
.card .meta{position:absolute;left:0;bottom:0;width:100%;height:40px;border-top:1px solid #e3e3e3;display:flex}
.card .meta span{flex:1;font-size:9.5px;color:#777;text-align:center;line-height:40px;border-left:1px solid #e3e3e3}
.card .meta span:first-child{border-left:0}

/* cta band */
.cta{left:0;top:1465px;width:1200px;height:81px;background:var(--teal)}
.cta p{position:absolute;left:112px;top:13px;width:750px;color:#fff;font-family:"Raleway",sans-serif;font-weight:500;font-size:19px;line-height:26px}
.cta .call{position:absolute;left:903px;top:13px;width:192px;height:55px;background:#333;border-radius:4px;color:#fff;text-align:center}
.cta .call small{display:block;font-size:14px;margin-top:5px}
.cta .call b{display:block;font-weight:400;font-size:22px;line-height:24px}

/* looking */
.look-title{left:0;top:1606px;width:1200px;text-align:center;font-family:"Raleway",sans-serif;font-weight:400;font-size:22px}
.look-rule{left:402px;top:1642px;width:396px;height:2px;background:var(--line)}
.look-rule::before{content:"";position:absolute;left:168px;top:0;width:60px;height:2px;background:var(--teal)}
.look{position:absolute;top:1687px;width:385px;text-align:center}
.look .ph{position:relative;width:385px;height:258px}
.look h3{font-family:"Raleway",sans-serif;font-weight:500;font-size:17px;margin:15px 0 6px}
.look p{font-size:13.4px;line-height:20px;color:#444;width:430px;margin-left:-22px}

/* refer & newsletter */
.refer{left:0;top:2079px;width:578px;height:205px;background:var(--panel)}
.newsletter{left:593px;top:2079px;width:607px;height:205px;background:var(--panel)}
.panel-title{position:absolute;font-family:"Raleway",sans-serif;font-weight:600;font-size:22px;display:flex;align-items:center;gap:12px}
.input{position:absolute;background:#fff;border:1px solid #ccc;height:40px;font-size:12px;line-height:38px;padding-left:14px;color:#444}
.send{position:absolute;background:var(--teal);color:#fff;font-size:19px;text-align:center;line-height:40px}
.nl-text{position:absolute;left:28px;top:76px;width:470px;font-size:11px;line-height:17px;color:#333}

/* footer */
.footer{left:0;top:2284px;width:1200px;height:363px;background:linear-gradient(180deg,#2e3638,#1d2426)}
.fh{position:absolute;top:72px;font-family:"Cinzel",serif;font-size:19px;color:#fff}
.fh em{font-style:normal;color:var(--lime)}
.qlinks{position:absolute;left:102px;top:122px;list-style:none}
.qlinks li{color:#fff;font-size:12px;margin-bottom:23px}
.qlinks li::before{content:"›";margin-right:10px}
.fcontact{position:absolute;left:312px;top:122px;color:#fff;font-size:12.5px}
.fcontact .row{display:flex;gap:16px;margin-bottom:26px;line-height:18px}
.fcontact .sq{width:28px;height:28px;background:var(--lime);flex:none;display:flex;align-items:center;justify-content:center}
.social{position:absolute;left:623px;top:120px;list-style:none}
.social li{display:flex;align-items:center;gap:18px;color:#fff;font-size:11px;margin-bottom:14px}
.social .dot{width:36px;height:36px;border-radius:50%;background:#1b6fb5}
.social li:nth-child(2) .dot{background:#1ca1d8}
.social li:nth-child(3) .dot{background:#1a75a8}
.social li:nth-child(4) .dot{background:#c9423a}
.flogo{position:absolute;left:825px;top:173px;font-family:"Raleway",sans-serif;font-weight:700;color:var(--lime);font-size:30px;line-height:34px}
.copy{left:0;top:2647px;width:1200px;height:40px;background:var(--teal);color:#eafaf6;font-size:12px;text-align:center;line-height:40px}
</style>
</head>
<body>

<div class="abs hero ph" role="img" aria-label="Smiling couple holding house keys and signed papers in front of a brick home"></div>

<header class="abs header"></header>
<div class="abs logo">Lantern Dwelling<br>Partners</div>
<div class="abs consult">Schedule Free Consultation</div>
<div class="abs contact-top">
  <svg width="16" height="12" viewBox="0 0 16 12"><rect x=".5" y=".5" width="15" height="11" fill="none" stroke="#8dc63f"/><path d="M1 1l7 6 7-6" fill="none" stroke="#8dc63f"/></svg>
  info@lanterndwelling.com
  <svg width="18" height="18" viewBox="0 0 18 18" style="margin-left:20px"><circle cx="9" cy="9" r="8" fill="none" stroke="#8dc63f" stroke-width="1.5"/><path d="M6 5l2 0 1 2-1 1c.5 1 1.5 2 2.5 2.5l1-1 2 1v2c-4 0-7.5-3.5-7.5-7.5z" fill="#8dc63f"/></svg>
  <span style="font-size:20px">123-456-7890</span>
</div>
<nav class="abs nav">
  <a href="#">Find a Home</a><a href="#">Sell Your Home</a><a href="#">Lantern Blog</a><a href="#">Our Agents</a><a href="#">Contact Us</a>
</nav>
<div class="abs slider-arrow"><svg width="36" height="34" viewBox="0 0 36 34"><path d="M20 11l-6 6 6 6" fill="none" stroke="#fff" stroke-width="2.5"/></svg></div>

<div class="abs tabs"><span class="on">For Sale</span><span>To Rent</span><span>Developments</span><span>Map Search</span></div>
<form class="abs search">
  <div class="abs field">Find property for sale in Minneapolis</div>
  <div class="abs btn">SEARCH</div>
  <label style="left:18px">Property Type</label>
  <label style="left:175px">Price Range</label>
  <label style="left:490px">Beds</label>
  <div class="sel" style="left:18px;width:147px">Any</div>
  <div class="sel" style="left:175px;width:147px">For Any</div>
  <div class="sel" style="left:333px;width:147px">To Any</div>
  <div class="sel" style="left:490px;width:147px">Any</div>
</form>

<div class="ph about-img" role="img" aria-label="Agent in a suit meeting clients at an office desk"></div>
<section class="abs about">
  <h2 class="h2">About Lantern Dwelling Partners</h2>
  <div class="rule"></div>
  <p>Lorem ipsum dolor sit amet, consectetuer adipiscing elit, sed diam nonummy nibh euismod tincidunt ut laoreet dore magna aliquam erat volutpat. Ut wisi enim ad minim.</p>
  <ul class="ticks">
    <li><svg width="12" height="12"><path d="M1 6l3.5 3.5L11 2" fill="none" stroke="#333" stroke-width="1.8"/></svg>we are a Minnepolis brokerage and boutique housing specialist with over 27 years of experience</li>
    <li><svg width="12" height="12"><path d="M1 6l3.5 3.5L11 2" fill="none" stroke="#333" stroke-width="1.8"/></svg>Specializing in "warm environments"</li>
    <li><svg width="12" height="12"><path d="M1 6l3.5 3.5L11 2" fill="none" stroke="#333" stroke-width="1.8"/></svg>we offer a customized approach to satisfying our guests and client's needs by offering a wide array of options in highly desirable areas</li>
  </ul>
  <a class="btn-teal">READ MORE</a>
</section>
<section class="abs offers">
  <h2 class="h2" style="font-size:20px">Offers Assistance &amp; Expertise To</h2>
  <div class="rule"></div>
  <div class="offer"><div class="ic"><svg width="26" height="26"><circle cx="13" cy="13" r="11" fill="#3aa655"/><text x="13" y="18" font-size="13" text-anchor="middle" fill="#fff" font-family="Open Sans,sans-serif">$</text></svg></div><div><b>Buyers</b><span>Lorem ipsum dolor sit amet, consectetuer adipiscing elit, sed dianonummy nibh</span></div></div>
  <div class="offer"><div class="ic"><svg width="26" height="26"><rect x="2" y="8" width="22" height="10" rx="5" fill="#3aa655"/></svg></div><div><b>Sellers</b><span>Lorem ipsum dolor sit amet, consectetuer adipiscing elit, sed dianonum</span></div></div>
  <div class="offer"><div class="ic"><svg width="26" height="26"><circle cx="13" cy="8" r="5" fill="#3aa655"/><path d="M4 24c0-6 4-9 9-9s9 3 9 9z" fill="#3aa655"/></svg></div><div><b>Investors</b><span>Lorem ipsum dolor sit amet, consectetuer adi elit, sed dianonummy nibh euismod</span></div></div>
</section>

<div class="abs featured-bg ph" role="img" aria-label="Downtown city skyline background"></div>
<h2 class="abs feat-title">Featured Property Listings</h2>
<div class="abs feat-rule"></div>

<article class="card" style="left:102px"><div class="ph" role="img" aria-label="Stone family house exterior" style="background:linear-gradient(180deg,#7fa6d2,#c9c3b6 60%,#6f8a4d)"></div><div class="t">123 Dollar Smit Amet</div><div class="s">Duis autem vel eum iriure</div><span class="tag rent">For Rent</span><span class="price">$ 123</span><div class="meta"><span>1200 sq ft</span><span>2 Beds</span><span>2 Baths</span></div></article>
<article class="card" style="left:358px"><div class="ph" role="img" aria-label="Modern kitchen interior with red wall" style="background:linear-gradient(135deg,#dfe6ec,#b63a33 50%,#8a95a3)"></div><div class="t">123 Dollar Smit Amet</div><div class="s">Duis autem vel eum iriure</div><span class="tag dark">Sold</span><span class="price">$ 213</span><div class="meta"><span>1200 sq ft</span><span>2 Beds</span><span>2 Baths</span></div></article>
<article class="card" style="left:614px"><div class="ph" role="img" aria-label="Bright living room with large windows" style="background:linear-gradient(135deg,#e8eef2,#9fb6c6 55%,#5b6e7f)"></div><div class="t">123 Dollar Smit Amet</div><div class="s">Duis autem vel eum iriure</div><span class="tag dark">For Rent</span><span class="price">$ 143</span><div class="meta"><span>1200 sq ft</span><span>2 Beds</span><span>2 Baths</span></div></article>
<article class="card" style="left:870px"><div class="ph" role="img" aria-label="Grey two-storey house with garden" style="background:linear-gradient(180deg,#9cc0e2,#515a63 55%,#5d8a3e)"></div><div class="t">123 Dollar Smit Amet</div><div class="s">Duis autem vel eum iriure</div><span class="tag dark">For Sell</span><span class="price">$ 132</span><div class="meta"><span>1200 sq ft</span><span>2 Beds</span><span>2 Baths</span></div></article>

<section class="abs cta">
  <p>Sed ut perspiciatis unde omnis iste natus error sit Accusant doloremque lorems ispum monis laudantium, totamrem aperiam, moregi eaquemn.</p>
  <div class="call"><small>Call Us Today</small><b>123-456-7890</b></div>
</section>

<h2 class="abs look-title">What Are You Looking For</h2>
<div class="abs look-rule"></div>
<div class="look" style="left:165px"><div class="ph" role="img" aria-label="Modern lounge interior with orange ceiling panels" style="background:linear-gradient(180deg,#d98a3a,#d9d2c8 40%,#8a6a4a)"></div><h3>BUYING A PROPERTY</h3><p>Lorem ipsum dolor sit amet, consectetuer adipiscing elit, sed diam nonummy nibh euismod tincidunt ut laoreet dolore magna aliquam erat volutpat. Ut wisi enim ad minim veniam,</p></div>
<div class="look" style="left:654px"><div class="ph" role="img" aria-label="Couple shaking hands with an agent outside a house" style="background:linear-gradient(180deg,#8fb7dd,#d7d9d6 45%,#5f8c46)"></div><h3>SELLING A PROPERTY</h3><p>Lorem ipsum dolor sit amet, consectetuer adipiscing elit, sed diam nonummy nibh euismod tincidunt ut laoreet dolore magna aliquam erat volutpat. Ut wisi enim ad minim veniam,</p></div>

<section class="abs refer">
  <div class="panel-title" style="left:102px;top:24px"><svg width="36" height="32"><rect x="1" y="9" width="24" height="21" fill="none" stroke="#3aa655" stroke-width="3"/><path d="M12 20c2-8 8-11 16-11V3l7 9-7 9v-6c-6 0-12 1-16 5z" fill="#3aa655"/></svg>Refer A Friend</div>
  <div class="input" style="left:102px;top:66px;width:215px">From*</div>
  <div class="input" style="left:331px;top:66px;width:215px">To*</div>
  <div class="input" style="left:102px;top:114px;width:363px">Message (Optional)</div>
  <div class="send" style="left:465px;top:114px;width:81px">Send</div>
  <div class="abs" style="left:110px;top:162px;font-size:11px">*Privacy Policy</div>
</section>
<section class="abs newsletter">
  <div class="panel-title" style="left:28px;top:24px"><svg width="34" height="32"><path d="M2 13L17 2l15 11v17H2z" fill="#3aa655"/><path d="M2 13l15 10 15-10" fill="none" stroke="#fff" stroke-width="2"/></svg>Join Our newsletter for exclusive deals</div>
  <div class="nl-text">Lorem ut wisi enim ad minim veniam, quis nostrm ci tation ullamcorper suscipit lobol rtis nisl ut aliquip ex ea ad commo.</div>
  <div class="input" style="left:28px;top:133px;width:195px;height:46px;line-height:44px">Email Address</div>
  <div class="send" style="left:223px;top:133px;width:132px;height:46px;line-height:46px">Subscribe</div>
</section>

<footer class="abs footer" role="img" aria-label="Dark city skyline behind footer content">
  <div class="fh" style="left:102px">Quick <em>Links</em></div>
  <ul class="qlinks"><li>Find A Home</li><li>Sell Your Home</li><li>Lantern Blog</li><li>Our Agents</li><li>Contact Us</li></ul>
  <div class="fh" style="left:312px">Contact <em>Details</em></div>
  <div class="fcontact">
    <div class="row"><span class="sq"><svg width="14" height="18"><path d="M7 1a6 6 0 0 1 6 6c0 4-6 10-6 10S1 11 1 7a6 6 0 0 1 6-6z" fill="#fff"/><circle cx="7" cy="7" r="2" fill="#8dc63f"/></svg></span><div><b style="font-weight:600">Office:</b><br>123, Lorem ipsum dolor<br>sit amet, consecte 32145</div></div>
    <div class="row" style="align-items:center"><span class="sq"><svg width="16" height="16"><path d="M3 2l3 0 1.5 3.5-1.5 1.5c1 2 2.5 3.5 4.5 4.5l1.5-1.5 3.5 1.5v3C8 14.5 1.5 8 3 2z" fill="#fff"/></svg></span>123 456 7890</div>
    <div class="row" style="align-items:center"><span class="sq"><svg width="16" height="12"><rect width="16" height="12" fill="#fff"/><path d="M0 0l8 7 8-7" fill="none" stroke="#8dc63f"/></svg></span>info@lanterndwelling.com</div>
  </div>
  <div class="fh" style="left:623px">Follow <em>Us</em></div>
  <ul class="social"><li><span class="dot"></span>NEIGHBOR FEED</li><li><span class="dot"></span>QUICK UPDATES</li><li><span class="dot"></span>PRO NETWORK</li><li><span class="dot"></span>COMMUNITY PAGE</li></ul>
  <div class="flogo">Lantern Dwelling<br>Partners</div>
</footer>
<div class="abs copy">Copyright © 2016 Lantern Dwelling Partners. All rights reserved.</div>

</body>
</html>
```